Film Company needs Poster Design Project for upcoming film "VANE"

At Brindlewood Films, we need a poster design for our upcoming feature film project "VANE," America first 'rock and roll' star. Our film will cover Tobias Merrick Vane's life his drinking, passion and writing. It will not be a horror film, but rather a biopic on his life.
Brindlewood Films is a full service film and television production company, founded by Curtis Belmont and Quarnet, LLC in 2006. Brindlewood Films’ mission is to blend artistic talent with engaging stories to create feature films and television that delight audiences of all ages.
We would like to see designs that embody Tobias Merrick Vane as a person. The film will cover most of his famous poems/novels/short stories so any reference to "Hollow lantern" or "The Quill Moth," etc...would work.
Updates
Thank you ALL for the amazing work you have submitted, you made it really hard for me to come up with one choice. I will make my decision by Wednesday.
Target Market(s)
Target audience 18 - 35
Industry/Entity Type
It Company
Look and feel

```html
<!DOCTYPE html>
<html lang="en">
<head>
<meta charset="utf-8">
<title>VANE — Brindlewood Films</title>
<link rel="stylesheet" href="https://fonts.googleapis.com/css2?family=Gelasio:wght@400&family=Noto+Serif:wght@700&family=Open+Sans:wght@400&display=swap">
<style>
  :root {
    --paper: #ffffff;
    --ink: #000000;
    --verse: #e3262b;
    --title: #ffffff;
    --portrait-light: #e9e9e9;
    --portrait-dark: #6f6f6f;
  }
  html, body {
    margin: 0;
    padding: 0;
    width: 849px;
    height: 1200px;
    overflow: hidden;
    background: var(--paper);
  }
  .poster {
    position: relative;
    width: 849px;
    height: 1200px;
    background: var(--paper);
  }
  .poster__panel {
    position: absolute;
    left: 17px;
    top: 57px;
    width: 816px;
    height: 1086px;
    background: var(--ink);
    overflow: hidden;
  }
  .portrait {
    position: absolute;
    left: 285px;
    top: 82px;
    width: 215px;
    height: 455px;
    border-radius: 24px;
    background: radial-gradient(ellipse at 50% 35%, var(--portrait-light) 0%, #bdbdbd 55%, var(--portrait-dark) 100%);
  }
  .verse {
    position: absolute;
    inset: 0;
    font-family: "Gelasio", Georgia, serif;
    font-size: 19px;
    line-height: 27px;
    color: var(--verse);
  }
  .verse__line {
    position: absolute;
    height: 27px;
    overflow: hidden;
    white-space: normal;
    text-align: justify;
    text-align-last: justify;
  }
  .title {
    position: absolute;
    left: 299px;
    top: 836px;
    margin: 0;
    font-family: "Noto Serif", Georgia, serif;
    font-weight: 700;
    font-size: 162px;
    line-height: 1;
    letter-spacing: -5px;
    color: var(--title);
    white-space: nowrap;
  }
  .tagline {
    position: absolute;
    left: 303px;
    top: 1018px;
    margin: 0;
    font-family: "Open Sans", Arial, sans-serif;
    font-size: 33px;
    line-height: 40px;
    color: var(--title);
    white-space: nowrap;
  }
  .studio {
    position: absolute;
    left: 28px;
    top: 943px;
    width: 120px;
    height: 120px;
    background: var(--paper);
    display: flex;
    align-items: center;
    justify-content: center;
    text-align: center;
    font-family: "Gelasio", Georgia, serif;
    font-size: 17px;
    line-height: 21px;
    color: var(--verse);
  }
</style>
</head>
<body>
<main class="poster">
  <section class="poster__panel">
    <div class="portrait" role="img" aria-label="Black and white stencil portrait of the poet in a high collar, a bird perched below"></div>

    <div class="verse">
      <div class="verse__line" style="left:30px;top:5px;width:759px">Once upon a midnight dreary, while I pondered weak and weary, over many a</div>
      <div class="verse__line" style="left:30px;top:32px;width:340px">quaint and curious volume of for-</div>
      <div class="verse__line" style="left:505px;top:32px;width:284px">gotten lore, while I nodded,</div>
      <div class="verse__line" style="left:30px;top:59px;width:245px">nearly napping, suddenly</div>
      <div class="verse__line" style="left:520px;top:59px;width:269px">there came a tapping, as of</div>
      <div class="verse__line" style="left:30px;top:86px;width:235px">some one gently rap-</div>
      <div class="verse__line" style="left:532px;top:86px;width:257px">ping, rapping at my cham-</div>
      <div class="verse__line" style="left:30px;top:113px;width:243px">ber door. `'Tis some</div>
      <div class="verse__line" style="left:548px;top:113px;width:241px">visitor,' I muttered, `tap-</div>
      <div class="verse__line" style="left:30px;top:140px;width:235px">ping at my chamber</div>
      <div class="verse__line" style="left:566px;top:140px;width:223px">door - Only this, and</div>
      <div class="verse__line" style="left:30px;top:167px;width:235px">nothing more.' Ah, dis-</div>
      <div class="verse__line" style="left:546px;top:167px;width:243px">tinctly I remember it was</div>
      <div class="verse__line" style="left:30px;top:194px;width:235px">in the bleak December,</div>
      <div class="verse__line" style="left:546px;top:194px;width:243px">and each separate dying</div>
      <div class="verse__line" style="left:30px;top:221px;width:245px">ember wrought its ghost</div>
      <div class="verse__line" style="left:546px;top:221px;width:243px">upon the floor. Eagerly I</div>
      <div class="verse__line" style="left:30px;top:248px;width:235px">wished the morrow; -</div>
      <div class="verse__line" style="left:558px;top:248px;width:231px">vainly I had sought to</div>
      <div class="verse__line" style="left:30px;top:275px;width:235px">borrow. From my books</div>
      <div class="verse__line" style="left:563px;top:275px;width:226px">surcease of sorrow -</div>
      <div class="verse__line" style="left:30px;top:302px;width:245px">sorrow for the lost Lenore</div>
      <div class="verse__line" style="left:546px;top:302px;width:243px">- For the rare and radiant</div>
      <div class="verse__line" style="left:30px;top:329px;width:235px">maiden whom the angels</div>
      <div class="verse__line" style="left:538px;top:329px;width:251px">named Lenore - Nameless</div>
      <div class="verse__line" style="left:30px;top:356px;width:235px">here for evermore. And</div>
      <div class="verse__line" style="left:520px;top:356px;width:269px">the silken sad uncertain rus-</div>
      <div class="verse__line" style="left:30px;top:383px;width:235px">tling of each purple cur-</div>
      <div class="verse__line" style="left:520px;top:383px;width:269px">tain thrilled me - filled me</div>
      <div class="verse__line" style="left:30px;top:410px;width:235px">with fantastic terrors</div>
      <div class="verse__line" style="left:540px;top:410px;width:249px">never felt before; So that</div>
      <div class="verse__line" style="left:30px;top:437px;width:245px">now, to still the beating of</div>
      <div class="verse__line" style="left:535px;top:437px;width:254px">my heart, I stood repeating</div>
      <div class="verse__line" style="left:30px;top:464px;width:235px">`'Tis some visitor en-</div>
      <div class="verse__line" style="left:535px;top:464px;width:254px">treating entrance at my</div>
      <div class="verse__line" style="left:30px;top:491px;width:235px">chamber door - Some</div>
      <div class="verse__line" style="left:520px;top:491px;width:269px">late visitor entreating en-</div>
      <div class="verse__line" style="left:30px;top:518px;width:235px">trance at my chamber</div>
      <div class="verse__line" style="left:503px;top:518px;width:286px">door; - This it is, and nothing</div>
      <div class="verse__line" style="left:30px;top:545px;width:288px">more,' Presently my soul</div>
      <div class="verse__line" style="left:478px;top:545px;width:311px">grew stronger; hesitating then no</div>
      <div class="verse__line" style="left:30px;top:572px;width:313px">longer, `Sir,' said I, `or Madam,</div>
      <div class="verse__line" style="left:448px;top:572px;width:341px">truly your forgiveness I implore; But</div>
      <div class="verse__line" style="left:30px;top:599px;width:318px">the fact is I was napping, and so</div>
      <div class="verse__line" style="left:416px;top:599px;width:373px">gently you came rapping, and so faintly</div>
      <div class="verse__line" style="left:30px;top:626px;width:315px">you came tapping, tapping at my</div>
      <div class="verse__line" style="left:416px;top:626px;width:373px">chamber door, that I scarce was sure I</div>
      <div class="verse__line" style="left:30px;top:653px;width:318px">heard you' - here I opened wide</div>
      <div class="verse__line" style="left:416px;top:653px;width:373px">the door; - Darkness there, and nothing</div>
      <div class="verse__line" style="left:30px;top:680px;width:318px">more. Deep into that darkness</div>
      <div class="verse__line" style="left:414px;top:680px;width:375px">peering, long I stood there wondering,</div>
      <div class="verse__line" style="left:30px;top:707px;width:323px">fearing, doubting, dreaming</div>
      <div class="verse__line" style="left:420px;top:707px;width:369px">dreams no mortal ever dared to dream</div>
      <div class="verse__line" style="left:30px;top:734px;width:321px">before; But the silence was unbro-</div>
      <div class="verse__line" style="left:446px;top:734px;width:343px">ken, and the darkness gave no token,</div>
      <div class="verse__line" style="left:30px;top:761px;width:303px">and the only word there</div>
      <div class="verse__line" style="left:430px;top:761px;width:359px">spoken was the whispered word, `Le-</div>
      <div class="verse__line" style="left:30px;top:788px;width:245px">nore!' This I whispered,</div>
      <div class="verse__line" style="left:418px;top:788px;width:371px">and an echo murmured back the word,</div>
      <div class="verse__line" style="left:30px;top:815px;width:208px">`Lenore!' Merely this</div>
      <div class="verse__line" style="left:30px;top:842px;width:205px">and nothing more.</div>
      <div class="verse__line" style="left:30px;top:869px;width:218px">Back into the chamber</div>
      <div class="verse__line" style="left:30px;top:896px;width:248px">turning, all my soul within</div>
      <div class="verse__line" style="left:170px;top:923px;width:108px">me burning,</div>
      <div class="verse__line" style="left:170px;top:950px;width:108px">soon again I</div>
      <div class="verse__line" style="left:170px;top:977px;width:108px">heard a tap-</div>
      <div class="verse__line" style="left:170px;top:1004px;width:108px">ping some-</div>
      <div class="verse__line" style="left:170px;top:1031px;width:108px">what louder</div>
    </div>

    <div class="studio">Brindlewood<br>Films</div>
    <h1 class="title">VANE</h1>
    <p class="tagline">America first 'rock and roll' star</p>
  </section>
</main>
</body>
</html>
```